Boutique Real Estate Brokerage looking for business card, letterhead and envelope design

We are looking for a cohesive design for our business cards, letterhead and envelopes and that mirrors our high-end homes and clientele. Fern & Gable is being launched and designed for the marketplace of tomorrow. We grew from the #1 team in our community into a full-service firm that is going to revolutionize the traditional real estate model.

We understand that it’s more important than ever to help our clients and partners adapt to behavioral and market changes being driven by generational shifts and technological advances in society, and by combining traditional brokerage services with innovative production and marketing capabilities, we know how to do that better than anyone else.

Requirements
Must have
• business card, letterhead and envelope design - attached logo.

```html
<!DOCTYPE html>
<html lang="en">
<head>
<meta charset="utf-8">
<title>Fern &amp; Gable Realty – Stationery</title>
<link href="https://fonts.googleapis.com/css2?family=Montserrat:wght@500;600&family=Open+Sans:wght@400;600&display=swap" rel="stylesheet">
<style>
:root{
  --bg:#d6d6d8;
  --paper:#ffffff;
  --indigo:#1b0c5c;
  --indigo-deep:#140848;
  --indigo-soft:#2a1a78;
  --gold:#c49a5e;
  --ink:#4a4a55;
  --ink-light:#8a8a96;
}
*{margin:0;padding:0;box-sizing:border-box}
html,body{width:1200px;height:800px;overflow:hidden;background:var(--bg)}
body{position:relative;font-family:"Open Sans",sans-serif;color:var(--ink)}
.piece{position:absolute;box-shadow:0 2px 5px rgba(0,0,0,.18);overflow:hidden}
.brand{display:flex;align-items:center;gap:4px;font-family:"Montserrat",sans-serif;font-weight:600;color:var(--indigo);white-space:nowrap}
.brand-mark{background:var(--gold);display:block;flex:none}
.brand.on-dark{color:var(--gold)}
.band{position:absolute;left:0;bottom:0;width:100%;display:block}

/* letterhead */
.letterhead{left:259px;top:88px;width:208px;height:294px;background:var(--paper)}
.letterhead .brand{position:absolute;left:18px;top:24px;font-size:7px}
.letterhead .brand-mark{width:7px;height:7px}
.lh-contact{position:absolute;left:139px;top:18px;font-size:3.8px;line-height:5.2px;color:var(--ink)}
.lh-contact .icon{display:inline-block;width:3px;height:3px;border-radius:50%;background:var(--indigo);margin-right:2px;vertical-align:middle}
.lh-body{position:absolute;left:18px;top:68px;width:172px;font-size:3.7px;line-height:5.6px;color:var(--ink);text-align:justify}
.lh-body p{margin-bottom:6px}
.signature{position:absolute;left:18px;top:218px;width:26px;height:20px;background:#f1f1f4}

/* envelopes */
.env-open{left:499px;top:128px;width:218px;height:149px;background:var(--paper)}
.env-window{left:742px;top:128px;width:218px;height:108px;background:var(--paper)}
.env-window .brand{position:absolute;left:17px;top:13px;font-size:6px}
.env-window .brand-mark{width:6px;height:6px}
.env-address{position:absolute;left:17px;top:25px;font-size:4.6px;line-height:5.8px}
.window{position:absolute;left:17px;top:67px;width:66px;height:28px;border:1px solid #dcdce4;border-radius:2px;background:linear-gradient(90deg,#f3f3f6,#ffffff)}
.env-closed{left:743px;top:269px;width:218px;height:109px;background:var(--paper)}
.env-closed .brand{position:absolute;left:50%;top:14px;transform:translateX(-50%);font-size:7px}
.env-closed .brand-mark{width:7px;height:7px}

/* business cards */
.card-front{left:503px;top:325px;width:85px;height:55px;background:var(--paper)}
.card-front .brand{position:absolute;left:7px;top:24px;font-size:3.6px;gap:2px}
.card-front .brand-mark{width:4px;height:4px}
.card-rule{position:absolute;left:44px;top:13px;width:.5px;height:28px;background:#c9c9d2}
.card-details{position:absolute;left:46px;top:14px;font-size:2.2px;line-height:3.2px}
.card-name{font-family:"Montserrat",sans-serif;font-weight:600;color:var(--gold);font-size:2.6px}
.card-back{left:622px;top:325px;width:84px;height:55px;background:var(--indigo)}
.card-back .pattern{position:absolute;inset:0;background:linear-gradient(135deg,var(--indigo-soft),var(--indigo-deep))}

/* folders */
.folder-front{left:242px;top:412px;width:226px;height:305px;background:var(--indigo)}
.folder-front .brand{position:absolute;left:50%;top:160px;transform:translateX(-50%);font-size:17px;gap:8px}
.folder-front .brand-mark{width:14px;height:14px}
.folder-url{position:absolute;left:0;width:100%;top:276px;text-align:center;font-family:"Montserrat",sans-serif;font-weight:500;font-size:8.5px;letter-spacing:1px;color:#d8d6e6}
.folder-url span{color:var(--gold)}
.folder-open{left:502px;top:410px;width:455px;height:303px;background:var(--indigo)}
.folder-open .pattern{position:absolute;left:0;top:0;width:100%;height:205px;background:linear-gradient(180deg,#1f1064,#1a0b58)}
.pocket{position:absolute;top:205px;height:98px;background:var(--indigo-deep);box-shadow:0 -2px 4px rgba(0,0,0,.25)}
.pocket.left{left:0;width:224px}
.pocket.right{left:231px;width:224px}
.spine{position:absolute;left:226px;top:0;width:2px;height:100%;background:rgba(0,0,0,.25)}
.pocket .brand{position:absolute;right:28px;top:44px;font-size:13px;gap:6px}
.pocket .brand-mark{width:11px;height:11px}
</style>
</head>
<body>

<!-- Letterhead -->
<section class="piece letterhead" aria-label="Letterhead">
  <div class="brand"><span class="brand-mark"></span>Fern &amp; Gable</div>
  <div class="lh-contact">
    48 Alder Crest Lane,<br>Maple Grove, ON L7K 3P2<br>
    <span class="icon"></span>+15550142687<br>
    <span class="icon"></span>mara@fernandgable.com<br>
    <span class="icon"></span>www.fernandgable.com
  </div>
  <div class="lh-body">
    <p>Dear customer,</p>
    <p>Lorem ipsum dolor sit amet, consectetur adipisicing elit, sed do eiusmod tempor incididunt ut labore et dolore magna aliqua. Ut enim ad minim veniam, quis nostrud exercitation ullamco laboris nisi ut aliquip ex ea commodo consequat. Duis aute irure dolor in reprehenderit in voluptate velit esse cillum dolore eu fugiat nulla pariatur. Excepteur sint occaecat cupidatat non proident, sunt in culpa qui officia deserunt mollit anim id est laborum.</p>
    <p>Lorem ipsum dolor sit amet, consectetur adipisicing elit, sed do eiusmod tempor incididunt ut labore et dolore magna aliqua. Ut enim ad minim veniam, quis nostrud exercitation ullamco laboris nisi ut aliquip ex ea commodo consequat. Duis aute irure dolor in reprehenderit in voluptate velit esse cillum dolore eu fugiat nulla pariatur. Excepteur sint occaecat cupidatat non proident, sunt in culpa qui officia deserunt mollit anim id est laborum.</p>
    <p>Lorem ipsum dolor sit amet, consectetur adipisicing elit, sed do eiusmod tempor incididunt ut labore et dolore magna aliqua. Ut enim ad minim veniam, quis nostrud exercitation ullamco laboris nisi ut aliquip ex ea commodo consequat. Duis aute irure dolor in reprehenderit in voluptate velit esse cillum dolore eu fugiat nulla pariatur. Excepteur sint occaecat cupidatat non proident, sunt in culpa qui officia deserunt mollit anim id est laborum.</p>
    <p>Lorem ipsum dolor sit amet, consectetur adipisicing elit, sed do eiusmod tempor incididunt ut labore et dolore magna aliqua. Ut enim ad minim veniam, quis nostrud exercitation ullamco laboris nisi ut aliquip ex ea commodo consequat. Duis aute irure dolor in reprehenderit.</p>
    <p>Yours Sincerely,</p>
  </div>
  <div class="signature" role="img" aria-label="Handwritten signature"></div>
  <svg class="band" width="208" height="5" viewBox="0 0 208 5" aria-hidden="true">
    <polygon points="0,0 126,0 122,5 0,5" fill="var(--indigo)"/>
    <polygon points="128,0 208,0 208,5 124,5" fill="var(--gold)"/>
  </svg>
</section>

<!-- Envelope, back with open flap -->
<section class="piece env-open" aria-label="Envelope back, flap open">
  <svg width="218" height="149" viewBox="0 0 218 149" aria-hidden="true">
    <path d="M4,40 L8,4 Q9,0 13,0 L205,0 Q209,0 210,4 L214,40 Z" fill="var(--indigo-deep)"/>
    <rect x="0" y="40" width="218" height="25" fill="var(--paper)"/>
    <path d="M14,40 L204,40 L204,65 L14,65 Z" fill="var(--indigo-soft)"/>
    <path d="M0,40 L0,65 L14,65 L14,52 Q14,42 4,40 Z" fill="var(--paper)"/>
    <path d="M218,40 L218,65 L204,65 L204,52 Q204,42 214,40 Z" fill="var(--paper)"/>
  </svg>
</section>

<!-- Envelope, front with window -->
<section class="piece env-window" aria-label="Envelope front">
  <div class="brand"><span class="brand-mark"></span>Fern &amp; Gable</div>
  <div class="env-address">48 Alder Crest Lane,<br>Maple Grove, ON L7K 3P2</div>
  <div class="window"></div>
  <svg class="band" width="218" height="5" viewBox="0 0 218 5" aria-hidden="true">
    <polygon points="0,0 132,0 128,5 0,5" fill="var(--indigo)"/>
    <polygon points="134,0 218,0 218,5 130,5" fill="var(--gold)"/>
  </svg>
</section>

<!-- Envelope, back with closed flap -->
<section class="piece env-closed" aria-label="Envelope back, flap closed">
  <svg width="218" height="109" viewBox="0 0 218 109" aria-hidden="true" style="position:absolute;left:0;top:0">
    <path d="M0,0 L218,0 L212,36 Q211,41 205,41 L13,41 Q7,41 6,36 Z" fill="var(--indigo)"/>
  </svg>
  <div class="brand on-dark"><span class="brand-mark"></span>Fern &amp; Gable</div>
</section>

<!-- Business card front -->
<section class="piece card-front" aria-label="Business card front">
  <div class="brand"><span class="brand-mark"></span>Fern &amp; Gable</div>
  <div class="card-rule"></div>
  <div class="card-details">
    <div class="card-name">MARA ELLISON</div>
    Managing Director<br>
    48 Alder Crest Lane,<br>Maple Grove, ON L7K 3P2<br>
    555 010 2244<br>info@fernandgable.com<br>www.fernandgable.com
  </div>
  <svg class="band" width="85" height="2" viewBox="0 0 85 2" aria-hidden="true">
    <polygon points="0,0 42,0 41,2 0,2" fill="var(--gold)"/>
    <polygon points="43,0 85,0 85,2 42,2" fill="var(--indigo)"/>
  </svg>
</section>

<!-- Business card back -->
<section class="piece card-back" aria-label="Business card back">
  <div class="pattern" role="img" aria-label="Repeating monogram pattern in deep indigo"></div>
</section>

<!-- Presentation folder, closed -->
<section class="piece folder-front" aria-label="Presentation folder cover">
  <svg width="226" height="305" viewBox="0 0 226 305" aria-hidden="true" style="position:absolute;left:0;top:0">
    <path d="M0,250 Q90,120 226,78 L226,305 L0,305 Z" fill="#ffffff" opacity=".05"/>
  </svg>
  <div class="brand on-dark"><span class="brand-mark"></span>Fern &amp; Gable</div>
  <div class="folder-url">www.<span>fernandgable</span>.com</div>
</section>

<!-- Presentation folder, open -->
<section class="piece folder-open" aria-label="Presentation folder interior">
  <div class="pattern" role="img" aria-label="Repeating monogram pattern, tone on tone indigo"></div>
  <div class="spine"></div>
  <div class="pocket left"></div>
  <div class="pocket right">
    <div class="brand on-dark"><span class="brand-mark"></span>Fern &amp; Gable</div>
  </div>
</section>

</body>
</html>
```